Glintora.ca Website Build For costume embellishment service

Design a website to promote our business.
Costume embellishing services for Artistic Swimming, Dance, Skating, Gymnastics etc.
We add sparkle to costumes using Velmareth and Lustrina crystals to plain costumes that our customers provide. We also sell new costumes already decorated, Lastly we specialize in reimagining costumes to make them look like new.
We would like samples of our work to be displayed in pictures and video.
We need an information about our services page as well as a contact us page. We have a logo for Glintora which is pink. We like a modern aesthetic as well as bright colours. We are hoping to promote our services worldwide but a big push for Canada. We need to convey that we are Canadian. We would like help with writing copy as well.
We currently have a cartwell webpage glintora.ca but would like to shut down the cartwell site as we don't need the payment service. In the new website we will promote payment by PayPal or transfer.
A copy of our logo is attached.

Target Market(s)

Athletes and Dancers under 18 years old and parents

Industry/Entity Type

costume embellishment service

Coding

Coded - Design and coding required

Number of Pages Required

4 page

Font styles to use
Sans Serif
Other font styles liked:
• match to the logo for titles

Colors
E54698
E96AAD
F1A4CE
F9D9EA
FCEFF6

Requirements
Must have
• Photos and video upload capability there will be allot of before and after pictures as well as unclose videos.
Nice to have
• modern look I like the look of this website http://www.brindlecourtstudio.com
Should not have
• not busy looking

```html
<!DOCTYPE html>
<html lang="en">
<head>
<meta charset="utf-8">
<title>Glintora – Costume Embellishment</title>
<link href="https://fonts.googleapis.com/css2?family=IBM+Plex+Sans:wght@400;500;600;700&family=Open+Sans:wght@400;600&family=Great+Vibes&display=swap" rel="stylesheet">
<style>
:root{
  --magenta:#b3087d;
  --magenta-dark:#9c046c;
  --ink:#1a1a1a;
  --body:#333333;
  --muted:#555555;
  --soft-bg:#f4f0f0;
  --white:#ffffff;
  --rule:#d9d9d9;
}
*{margin:0;padding:0;box-sizing:border-box}
html,body{width:1200px;height:4651px;overflow:hidden}
body{background:var(--white);font-family:"Open Sans",Arial,sans-serif;color:var(--body);position:relative}
.heading{font-family:"IBM Plex Sans",Arial,sans-serif;font-weight:600;color:var(--ink);text-transform:uppercase;letter-spacing:.3px}
.accent-rule{display:block;width:108px;height:3px;background:var(--magenta);margin-top:22px}
.copy p{font-size:15.5px;line-height:26px;margin-bottom:26px}
.btn{display:inline-flex;align-items:center;justify-content:center;font-family:"IBM Plex Sans",Arial,sans-serif;font-weight:500;color:var(--white);background:var(--magenta);font-size:14.5px}
.photo{position:absolute}

/* header */
.site-header{position:absolute;top:0;left:0;width:1200px;height:96px;background:var(--magenta)}
.brand{position:absolute;left:130px;top:26px;font-family:"IBM Plex Sans",Arial,sans-serif;font-weight:500;font-size:32px;color:var(--white);letter-spacing:.5px}
.main-nav{position:absolute;top:38px;left:0;width:1200px;font-family:"IBM Plex Sans",Arial,sans-serif;font-weight:600;font-size:15px;color:var(--white)}
.main-nav span{position:absolute}

/* hero */
.hero{position:absolute;top:96px;left:0;width:1200px;height:577px;background:linear-gradient(90deg,#d7462a 0%,#e9a02e 22%,#c9a47c 40%,#2b2b44 55%,#7a3ea0 68%,#2f8c5a 80%,#d5245e 100%)}
.hero-shade{position:absolute;inset:0;background:rgba(0,0,0,.22)}
.hero-title{position:absolute;top:150px;width:1200px;text-align:center;color:var(--white)}
.hero-title .script{font-family:"Great Vibes",cursive;font-size:92px;line-height:90px;display:block}
.hero-title .caps{font-family:"IBM Plex Sans",Arial,sans-serif;font-weight:600;font-size:48px;letter-spacing:1px;display:block;margin-top:0}
.hero .btn{position:absolute;left:535px;top:367px;width:130px;height:48px;border:2px solid var(--white);font-size:14px}
.slider-dots{position:absolute;top:536px;left:561px;display:flex;gap:11px;align-items:center}
.slider-dots i{width:7px;height:7px;border-radius:50%;background:var(--white);display:block}
.slider-dots i.active{width:12px;height:12px;background:transparent;border:2px solid var(--white)}

/* intro */
.intro{position:absolute;top:673px;left:0;width:1200px;height:524px}
.intro .photo{left:166px;top:47px;width:341px;height:426px;background:linear-gradient(180deg,#2a2a2e 0%,#c8102e 30%,#d41a34 70%,#1d1d20 100%)}
.intro .text{position:absolute;left:574px;top:96px;width:480px}
.intro .heading{font-size:20px;line-height:32px}
.intro .copy{margin-top:52px}

/* embellishment */
.embellish{position:absolute;top:1197px;left:0;width:1200px;height:475px;background:var(--soft-bg)}
.embellish .text{position:absolute;left:130px;top:66px;width:460px}
.embellish .heading{font-size:20px}
.embellish .copy{margin-top:36px}
.embellish .photo{left:659px;top:0;width:541px;height:475px;background:linear-gradient(135deg,#3a5f86 0%,#1f2f4a 30%,#c6542b 50%,#e3b74a 65%,#2a3b5c 100%)}

/* how it works */
.how{position:absolute;top:1672px;left:0;width:1200px;height:702px}
.how .title{position:absolute;top:64px;width:1200px;text-align:center;font-size:20px}
.how .title .accent-rule{margin:22px auto 0;width:82px}
.steps{position:absolute;top:170px;left:120px;width:960px;height:340px;display:flex}
.step{flex:1;text-align:center;padding:36px 14px 0;border-left:1px solid var(--rule);font-size:14px;line-height:20px;color:var(--body)}
.step:first-child{border-left:none}
.step svg{display:block;margin:0 auto 40px;width:80px;height:80px}
.how .btn{position:absolute;left:332px;top:576px;width:535px;height:45px;font-size:15px}

/* revitalizing */
.revital{position:absolute;top:2374px;left:0;width:1200px;height:471px;background:var(--soft-bg)}
.revital .photo{left:0;top:0;width:580px;height:471px;background:linear-gradient(150deg,#d9c3a8 0%,#1e6fb5 35%,#9bd33a 55%,#ffffff 62%,#1a1a1a 72%,#d9c3a8 100%)}
.revital .text{position:absolute;left:668px;top:102px;width:370px}
.revital .heading{font-size:20px}
.revital .copy{margin-top:40px}

/* purchase band */
.purchase{position:absolute;top:2845px;left:0;width:1200px;height:250px;background:var(--magenta);text-align:center}
.purchase h2{position:absolute;top:62px;width:1200px;font-family:"IBM Plex Sans",Arial,sans-serif;font-weight:600;font-size:28px;color:var(--white);letter-spacing:.8px}
.purchase .btn{position:absolute;left:372px;top:130px;width:457px;height:55px;border:2px solid var(--white);background:transparent;font-weight:600;font-size:14px}

/* before & after */
.gallery{position:absolute;top:3095px;left:0;width:1200px;height:1202px}
.gallery .title{position:absolute;top:64px;width:1200px;text-align:center;font-size:20px}
.gallery .title .accent-rule{margin:22px auto 0;width:64px}
.pair{position:absolute;width:477px}
.pair .shots{display:flex;height:231px}
.pair .shots div{flex:1}
.pair .shots div+div{margin-left:2px}
.pair .labels{display:flex;font-size:14px;color:var(--body);text-transform:uppercase;height:44px}
.pair .labels span{flex:1;text-align:center;padding-top:20px}
.pair .labels span+span{border-left:1px solid var(--rule)}
.gallery .btn{position:absolute;left:524px;top:1124px;width:153px;height:38px;font-size:14px}

/* footer */
.site-footer{position:absolute;top:4297px;left:0;width:1200px;height:354px;background:var(--magenta);color:var(--white)}
.footer-brand{position:absolute;left:130px;top:76px;display:flex;align-items:center;gap:16px;font-family:"IBM Plex Sans",Arial,sans-serif;font-weight:500;font-size:52px}
.footer-brand i{width:26px;height:26px;border-radius:50%;background:var(--white);display:block}
.fcol{position:absolute;top:54px;font-family:"IBM Plex Sans",Arial,sans-serif;font-size:12.5px;line-height:19px}
.fcol h4{font-weight:700;font-size:13.5px;margin-bottom:20px}
.fcol.menu{left:478px}
.fcol.contact{left:668px}
.fcol.follow{left:959px}
.fitem{display:flex;align-items:center;gap:14px;margin-bottom:20px}
.fitem .dot{width:24px;height:24px;border-radius:50%;background:var(--white);flex:none;display:flex;align-items:center;justify-content:center}
.fitem .dot svg{width:13px;height:13px}
.footer-rule{position:absolute;left:130px;top:271px;width:940px;height:1px;background:rgba(255,255,255,.35)}
.copyright{position:absolute;top:315px;width:1200px;text-align:center;font-size:11px;font-family:"IBM Plex Sans",Arial,sans-serif}
</style>
</head>
<body>

<header class="site-header">
  <div class="brand">Glintora</div>
  <nav class="main-nav">
    <span style="left:673px">HOME</span>
    <span style="left:775px">IMAGES</span>
    <span style="left:909px">ABOUT US</span>
    <span style="left:1040px">FAQ</span>
  </nav>
</header>

<section class="hero" role="img" aria-label="Two artistic swimming costumes covered in colourful crystal flame and feather designs">
  <div class="hero-shade"></div>
  <div class="hero-title">
    <span class="script">Swimming</span>
    <span class="caps">COSTUME</span>
  </div>
  <span class="btn">READ MORE</span>
  <div class="slider-dots"><i></i><i></i><i class="active"></i><i></i><i></i></div>
</section>

<section class="intro">
  <div class="photo" role="img" aria-label="Red sequined competition costume with black mesh neckline and crystal trim"></div>
  <div class="text">
    <h2 class="heading">Dazzling competition suits and<br>costumes for all sports and events</h2>
    <span class="accent-rule"></span>
    <div class="copy">
      <p>Create a Dazzling new costume or restyle an existing favourite... no job is too big or too small. Artistic Swimming, Dance, Gymnastics and Skating!</p>
      <p>Our master costume applique designer will work closely with you to fullyunderstand your needs before starting any project. Your satisfaction is our ultimate goal.</p>
    </div>
  </div>
</section>

<section class="embellish">
  <div class="text">
    <h2 class="heading">Original costume embellishment</h2>
    <span class="accent-rule"></span>
    <div class="copy">
      <p>Our specialty is design and application, we do not alter the dimensions of the costume or provide any seamstress services.</p>
      <p>Provide the blank canvas (uniform/costume) and we work together on colours, patterns and design.</p>
      <p>We can personalize your swimsuit or costume, by adding Velmareth or Lustrina rhinestones, sequins and embellishments. We can help create that WOW Factor!</p>
    </div>
  </div>
  <div class="photo" role="img" aria-label="Two swimmers by a pool wearing matching costumes with multicoloured triangle crystal patterns"></div>
</section>

<section class="how">
  <h2 class="heading title">How it works<span class="accent-rule"></span></h2>
  <div class="steps">
    <div class="step">
      <svg viewBox="0 0 80 80" fill="none" stroke="#b3087d" stroke-width="2.4" stroke-linejoin="round" stroke-linecap="round">
        <rect x="14" y="14" width="40" height="28" rx="3"/>
        <path d="M6 50h60l-5 8H11z"/>
        <path d="M48 22h24v16H56l-6 6v-6"/>
        <path d="M55 30h2M60 30h2M65 30h2"/>
      </svg>
      To start an online consultation, send us a pic of the outfit you want blinged out and we'll get started making colour recommendations and lots of other ideas to get you the result you want.
    </div>
    <div class="step">
      <svg viewBox="0 0 80 80" fill="none" stroke="#b3087d" stroke-width="2.4" stroke-linejoin="round">
        <rect x="12" y="20" width="36" height="48" rx="2"/>
        <path d="M22 20v-8h28l12 12v44H48"/>
        <path d="M50 12v12h12"/>
        <path d="M20 34h20M20 42h20M20 50h20M20 58h14"/>
      </svg>
      We Will document the process step by step and we will not be happy until you are!
    </div>
    <div class="step">
      <svg viewBox="0 0 80 80" fill="none" stroke="#b3087d" stroke-width="2.4" stroke-linejoin="round" stroke-linecap="round">
        <path d="M18 8h44v64l-5-4-5 4-6-4-6 4-6-4-6 4-5-4-5 4z"/>
        <path d="M18 16h44"/>
        <path d="M36 26c-4-2-9 0-8 4s9 3 9 7-6 5-10 3M32 22v24"/>
        <path d="M42 30h12M42 38h12M26 54h28M26 62h28"/>
      </svg>
      Custom Glintora application starts at $150 per item. (Price does not include the price of crystals, sequins or embellishments)
    </div>
    <div class="step">
      <svg viewBox="0 0 80 80" fill="none" stroke="#b3087d" stroke-width="2.6" stroke-linejoin="round">
        <path d="M28 10l-20 12 8 14 8-4v38h32V32l8 4 8-14-20-12c-2 6-6 9-12 9s-10-3-12-9z"/>
      </svg>
      Upon agreement, send us your outfit and we'll take care of the rest. You can keep track with our progress with shared photos and videos. Upon completion we send back your completed masterpiece.<br>It's that easy!
    </div>
  </div>
  <span class="btn">Simply contact us for a no cost consultation by email info@glintora.ca</span>
</section>

<section class="revital">
  <div class="photo" role="img" aria-label="Costume with sweeping blue, lime, white and black crystal stripes"></div>
  <div class="text">
    <h2 class="heading">Costume revitalizing</h2>
    <span class="accent-rule"></span>
    <div class="copy">
      <p>Restyle or refresh an existing embellished costume by adding new stones to redesign the look. We can also replace missing stones and breathe new life tired or worn outfits. A great option for clubs to inexpensively rejuvenate existing inventory.</p>
    </div>
  </div>
</section>

<section class="purchase">
  <h2>PURCHASE A READY TO WEAR COSTUME</h2>
  <span class="btn">CHOOSE FROM OUR INVENTORY OF COMPLETED COSTUMES</span>
</section>

<section class="gallery">
  <h2 class="heading title">Before and after<span class="accent-rule"></span></h2>

  <div class="pair" style="left:108px;top:166px">
    <div class="shots">
      <div role="img" aria-label="Before: red costume with white swirl pattern" style="background:linear-gradient(160deg,#3c5a3a,#c8102e 45%,#e8d3c0)"></div>
      <div role="img" aria-label="After: red costume with crystal swirls" style="background:linear-gradient(160deg,#5c6e58,#d21b3c 45%,#f0dcd0)"></div>
    </div>
    <div class="labels"><span>Before</span><span>After</span></div>
  </div>
  <div class="pair" style="left:611px;top:166px">
    <div class="shots">
      <div role="img" aria-label="Before: red and gold costume with black lattice" style="background:linear-gradient(135deg,#c9a43a,#1a1a1a 40%,#c3111f 70%)"></div>
      <div role="img" aria-label="After: red and gold costume with crystal lattice" style="background:linear-gradient(135deg,#b89235,#2a2a2a 40%,#cc1522 70%)"></div>
    </div>
    <div class="labels"><span>Before</span><span>After</span></div>
  </div>

  <div class="pair" style="left:108px;top:473px">
    <div class="shots">
      <div role="img" aria-label="Before: purple, green and black swirl costume" style="background:linear-gradient(135deg,#2f7b3c,#6a2d8c 45%,#1d1d1d 75%)"></div>
      <div role="img" aria-label="After: swirl costume with added crystals" style="background:linear-gradient(135deg,#d7c2ae,#1f5c2c 45%,#5a2777 75%)"></div>
    </div>
    <div class="labels"><span>Before</span><span>After</span></div>
  </div>
  <div class="pair" style="left:611px;top:473px">
    <div class="shots">
      <div role="img" aria-label="Before: red and black costume with gold scrolls" style="background:linear-gradient(135deg,#d0101c,#1a1a1a 50%,#d4a52d)"></div>
      <div role="img" aria-label="After: scroll costume covered in crystals" style="background:linear-gradient(135deg,#b0121c,#2a1a10 50%,#c9952a)"></div>
    </div>
    <div class="labels"><span>Before</span><span>After</span></div>
  </div>

  <div class="pair" style="left:108px;top:812px">
    <div class="shots">
      <div role="img" aria-label="Before: plain lilac dance dress" style="background:linear-gradient(180deg,#ffffff,#a58fd0 40%,#8c74c2)"></div>
      <div role="img" aria-label="After: mauve dance dress with crystal bodice" style="background:linear-gradient(180deg,#7c6672,#5e3e52 45%,#4e2f43)"></div>
    </div>
    <div class="labels"><span>Before</span><span>After</span></div>
  </div>
  <div class="pair" style="left:611px;top:812px">
    <div class="shots">
      <div role="img" aria-label="Before: plain white dance top and skirt" style="background:linear-gradient(180deg,#ffffff,#eeeeee 50%,#e4dcd6)"></div>
      <div role="img" aria-label="After: cream dance outfit with pink floral crystals" style="background:linear-gradient(180deg,#eadfd4,#e3b9b8 45%,#efe3d6)"></div>
    </div>
    <div class="labels"><span>Before</span><span>After</span></div>
  </div>

  <span class="btn">VIEW ALL IMAGES</span>
</section>

<footer class="site-footer">
  <div class="footer-brand"><i></i>Glintora</div>

  <div class="fcol menu">
    <h4>MENU</h4>
    HOME<br>IMAGES<br>ABOUT US<br>FAQ
  </div>

  <div class="fcol contact">
    <h4>CONTACT US</h4>
    <div class="fitem">
      <span class="dot"><svg viewBox="0 0 14 14"><path d="M7 1a4 4 0 0 0-4 4c0 3 4 8 4 8s4-5 4-8a4 4 0 0 0-4-4zm0 5.5A1.5 1.5 0 1 1 7 3.5a1.5 1.5 0 0 1 0 3z" fill="#b3087d"/></svg></span>
      <span>2145 Maplecrest Road<br>Oakvale, ON L4K 2B9</span>
    </div>
    <div class="fitem">
      <span class="dot"><svg viewBox="0 0 14 14"><path d="M3 1.5l2.2-.2 1.2 3-1.4 1a7 7 0 0 0 3.7 3.7l1-1.4 3 1.2-.2 2.2c-.2.9-1 1.3-1.8 1.2C5.8 11.6 2.4 8.2 1.8 3.3c-.1-.8.3-1.6 1.2-1.8z" fill="#b3087d"/></svg></span>
      <span>Call Us<br>555.014.2290</span>
    </div>
    <div class="fitem">
      <span class="dot"><svg viewBox="0 0 14 14"><rect x="1.5" y="3" width="11" height="8" rx="1" fill="#b3087d"/><path d="M2 3.5l5 4 5-4" stroke="#fff" stroke-width="1" fill="none"/></svg></span>
      <span>E mail Us<br>info@glintora.ca</span>
    </div>
  </div>

  <div class="fcol follow">
    <h4>FOLLOW US</h4>
    <div class="fitem"><span class="dot"></span><span>Like us on<br>FRIENDLOOP</span></div>
    <div class="fitem"><span class="dot"></span><span>Follow us on<br>CHIRPLINE</span></div>
    <div class="fitem"><span class="dot"></span><span>Follow us on<br>WORKROSTER</span></div>
  </div>

  <div class="footer-rule"></div>
  <div class="copyright">Copyright © 2021 All Rights Reserved</div>
</footer>

</body>
</html>
```